bluecastle aquatics of northeast florida business card

I need a new attractive business card. I am planning on printing on very thick rounded corner stock and having painted edges. We are a swimming pool remodel, repair, and service company in north florida. Our current logo is red, white, and blue. It doesn't necessarily have to stay that way, I am open to other ideas. It will need to contain my name, work and cell numbers, email, website, and my contractor license number.

Target Market(s)

High end residential and commercial clients

Industry/Entity Type

Business

Contact Information for Business Card

Company name, employee name and title, work and cell phone numbers, email and website, and Contractor number.

our work scope should be on card somewhere: remodel ~ repair ~ service

logo or slight variation of logo also. (not necessarily set on keeping exact logo)

Colors

Designer to choose colors to be used in the design.

Requirements
Nice to have
• We deal with water so I think some sort of water element or just a color similar to pool water would be nice to integrate into design.

```html
<!DOCTYPE html>
<html lang="en">
<head>
<meta charset="utf-8">
<title>Bluecastle Aquatics – Business Card</title>
<link rel="stylesheet" href="https://fonts.googleapis.com/css2?family=Libre+Baskerville:ital,wght@0,400;0,700;1,400&display=swap">
<style>
  :root {
    --pool-blue: #1877bd;
    --signal-red: #ec1c24;
    --ink-navy: #1d2a6b;
    --card-white: #ffffff;
    --backdrop: #e4e6ea;
    --divider: #9a9a9a;
  }
  * { margin: 0; padding: 0; box-sizing: border-box; }
  html, body {
    width: 1200px; height: 900px; overflow: hidden;
    background: var(--backdrop);
    font-family: "Libre Baskerville", Georgia, serif;
  }
  .canvas { position: relative; width: 1200px; height: 900px; }

  .card {
    position: absolute;
    width: 620px; height: 354px;
    background: var(--card-white);
    border-radius: 22px;
    overflow: hidden;
    box-shadow: 0 8px 24px rgba(0,0,0,0.18);
  }
  .card--back  { left: 510px; top: 60px; }
  .card--front { left: 70px;  top: 470px; }

  .card__waves { position: absolute; inset: 0; width: 100%; height: 100%; }

  .brand { position: absolute; display: flex; align-items: center; gap: 14px; }
  .brand__mark {
    width: 58px; height: 58px; border-radius: 50%;
    background: var(--pool-blue); flex: none;
  }
  .brand__name {
    color: var(--pool-blue); font-weight: 700;
    font-size: 24px; letter-spacing: 1px; line-height: 1.25;
  }
  .card--back .brand { left: 70px; top: 40px; }
  .card--front .brand { left: 36px; top: 32px; }

  .scope {
    position: absolute; left: 250px; top: 132px;
    color: var(--pool-blue); font-style: italic; font-size: 17px;
    letter-spacing: 0.5px;
  }

  .person {
    position: absolute; right: 368px; top: 150px; text-align: right;
  }
  .person__name { color: var(--ink-navy); font-weight: 700; font-size: 19px; }
  .person__title { color: var(--signal-red); font-size: 13px; margin-top: 4px; }

  .divider {
    position: absolute; left: 266px; top: 148px;
    width: 1px; height: 104px; background: var(--divider);
  }

  .contacts { position: absolute; left: 280px; top: 148px; list-style: none; }
  .contacts__item {
    display: flex; align-items: center; gap: 10px;
    height: 26px; color: var(--ink-navy); font-size: 15px;
  }
  .contacts__icon { width: 20px; height: 20px; flex: none; }

  .license {
    position: absolute; left: 34px; top: 300px;
    color: var(--card-white); font-size: 13px; letter-spacing: 0.5px;
    font-family: Arial, Helvetica, sans-serif;
  }
</style>
</head>
<body>
<main class="canvas">

  <section class="card card--back" aria-label="Card back">
    <svg class="card__waves" viewBox="0 0 620 354" aria-hidden="true">
      <path fill="var(--signal-red)" d="M0,150 C160,150 250,280 420,300 C520,310 580,300 620,292 L620,354 L0,354 Z"/>
      <path fill="var(--card-white)" d="M0,164 C160,164 250,294 420,314 C520,322 580,312 620,306 L620,354 L0,354 Z"/>
      <path fill="var(--pool-blue)" d="M0,172 C160,172 250,302 420,322 C520,330 580,320 620,314 L620,354 L0,354 Z"/>
    </svg>
    <div class="brand">
      <span class="brand__mark"></span>
      <div class="brand__name">Bluecastle Aquatics<br>of Northeast Florida</div>
    </div>
    <p class="scope">Remodel ~ Repair ~ Service</p>
  </section>

  <section class="card card--front" aria-label="Card front">
    <svg class="card__waves" viewBox="0 0 620 354" aria-hidden="true">
      <path fill="var(--signal-red)" d="M0,222 C150,222 260,310 410,318 C510,322 575,312 620,304 L620,354 L0,354 Z"/>
      <path fill="var(--card-white)" d="M0,236 C150,236 260,324 410,332 C510,336 575,326 620,318 L620,354 L0,354 Z"/>
      <path fill="var(--pool-blue)" d="M0,243 C150,243 260,331 410,339 C510,343 575,333 620,325 L620,354 L0,354 Z"/>
    </svg>
    <div class="brand">
      <span class="brand__mark"></span>
      <div class="brand__name">Bluecastle Aquatics<br>of Northeast Florida</div>
    </div>

    <div class="person">
      <div class="person__name">Daniel Whitfield</div>
      <div class="person__title">Managing Director</div>
    </div>

    <span class="divider"></span>

    <ul class="contacts">
      <li class="contacts__item">
        <svg class="contacts__icon" viewBox="0 0 20 20" aria-label="Work phone">
          <circle cx="10" cy="10" r="9" fill="none" stroke="var(--signal-red)" stroke-width="1.6"/>
          <path fill="var(--signal-red)" d="M6,7 Q6,5 8,5 L8.6,7.2 L7.6,8 Q8.6,10.6 11.6,12 L12.4,11 L14.6,11.8 Q14.6,14 12.4,14 Q6,12.6 6,7 Z"/>
        </svg>
        904.555.0147
      </li>
      <li class="contacts__item">
        <svg class="contacts__icon" viewBox="0 0 20 20" aria-label="Cell phone">
          <circle cx="10" cy="10" r="9" fill="none" stroke="var(--signal-red)" stroke-width="1.6"/>
          <rect x="7" y="4.5" width="6" height="11" rx="1.2" fill="var(--signal-red)"/>
          <rect x="8" y="6" width="4" height="6.5" fill="var(--card-white)"/>
        </svg>
        904.555.0193
      </li>
      <li class="contacts__item">
        <svg class="contacts__icon" viewBox="0 0 20 20" aria-label="Email">
          <circle cx="10" cy="10" r="9" fill="none" stroke="var(--signal-red)" stroke-width="1.6"/>
          <rect x="5" y="6.5" width="10" height="7" fill="var(--signal-red)"/>
          <path d="M5,6.5 L10,10.5 L15,6.5" fill="none" stroke="var(--card-white)" stroke-width="1"/>
        </svg>
        daniel@bluecastleaquatics.com
      </li>
      <li class="contacts__item">
        <svg class="contacts__icon" viewBox="0 0 20 20" aria-label="Website">
          <circle cx="10" cy="10" r="9" fill="none" stroke="var(--signal-red)" stroke-width="1.6"/>
          <circle cx="10" cy="10" r="5" fill="none" stroke="var(--signal-red)" stroke-width="1.2"/>
          <path d="M5,10 H15 M10,5 Q7,10 10,15 M10,5 Q13,10 10,15" fill="none" stroke="var(--signal-red)" stroke-width="1"/>
        </svg>
        www.bluecastleaquatics.com
      </li>
    </ul>

    <p class="license">Lic No : 0871526</p>
  </section>

</main>
</body>
</html>
```